Label for Whiskey and Rum Bottle

We are a distillery. Whiskey and Rum We like to have a new label for our bottles. The whiskey bottles are in a wooden case. http://www.korntropfen-muster.ch/store/product/tannwalder-oberkamm-single-malt-whiskey-nr-6 The Rum Bottles have no package. The label is even more important. http://www.korntropfen-muster.ch/store/product/tannwalder-oberkämmer-rum You can see the form of the bottles here www.korntropfen-muster.ch/store Whiskey and rum bottles are for a liter (50 cl) The labels can be with a picture or without. We would like to have something completely new. Therefore we don`t like to make much prescriptions concerning the design. We don`t like to give too much information (text) on the label. Just the information required by law. Consumers should understand the labels without long-reading. (The label-text is below) The 2 labels (Whiskey and rum) should look similar. Probably they have a different color or a different picture or .... It should be clear that the 2 products are from the same distillery. We have the intention to change all our existing labels over time. This gives designers the chance for follow-up projects.

Target Market(s)

Adults, liquor lovers

Requirements
Must have
• Information on the label is in German. (See "") Whiskey: - the name of the whiskey is "Tannwald Ridgeside Single Malt Whiskey" - The Whiskey was matured 5 years in a sherry "5 years in the sherry barrel stored" - The Alcohol content is 40% volumes "40% Vol "- The bottle contents 50 cl" 5 dl "- The distillery is" Distillery Brugghofer, Felsmatt, www.korntropfen-muster.ch "- The producer is" Korvix GmbH "Rum: - The name is" Tannwald Ridgesider Rum "- The alcohol content is 37% Volumes "37% Vol" - The bottle contens 50 cl "5 dl" - The distillery is "Distillery Brugghofer, Felsmatt, www.korntropfen-muster.ch" - The producer is "Korvix GmbH"
Nice to have
• Premium looking label Only front label preferred Only necessary text on the label
Should not have
• No special print techniques necessary No special paper form

```html
<!DOCTYPE html>
<html lang="de">
<head>
<meta charset="utf-8">
<title>Tannwalder Oberkämmer Rum – Etikett</title>
<link rel="stylesheet" href="https://fonts.googleapis.com/css2?family=Playfair+Display:wght@400;700&family=Arimo:wght@400&display=swap">
<style>
  :root {
    --page: #ffffff;
    --label-black: #0b0b0b;
    --label-edge: #1b1b1b;
    --gold: #c9a574;
    --gold-light: #e3c99d;
    --gold-dark: #a8834f;
    --band-light: #e6d3b3;
    --band-dark: #b89565;
  }
  * { margin: 0; padding: 0; box-sizing: border-box; }
  html, body {
    width: 1200px;
    height: 2700px;
    overflow: hidden;
    background: var(--page);
  }
  .canvas {
    position: relative;
    width: 1200px;
    height: 2700px;
  }
  .label {
    position: absolute;
    left: 150px;
    top: 835px;
    width: 900px;
    height: 1029px;
    background: radial-gradient(ellipse at 50% 45%, var(--label-black) 55%, var(--label-edge) 100%);
    box-shadow: 0 14px 30px rgba(0,0,0,0.18);
  }
  .label__band {
    position: absolute;
    left: 0;
    width: 100%;
    height: 17px;
    background: linear-gradient(90deg, var(--band-dark), var(--band-light) 50%, var(--band-dark));
  }
  .label__band--top { top: 0; }
  .label__band--bottom { bottom: 0; }
  .label__art {
    position: absolute;
    left: 0;
    top: 0;
    width: 900px;
    height: 1029px;
  }
  .label__text {
    position: absolute;
    left: 0;
    width: 100%;
    text-align: center;
    color: var(--gold);
  }
  .producer {
    top: 80px;
    font-family: "Playfair Display", serif;
    font-size: 33px;
    letter-spacing: 1.5px;
  }
  .product-name {
    top: 362px;
    font-family: "Playfair Display", serif;
    font-weight: 700;
    font-size: 60px;
    line-height: 66px;
    letter-spacing: 0.5px;
    color: var(--gold-light);
  }
  .distillery {
    top: 596px;
    font-family: "Arimo", sans-serif;
    font-size: 26px;
    line-height: 34px;
  }
  .footer {
    position: absolute;
    left: 25px;
    right: 30px;
    top: 962px;
    display: flex;
    justify-content: space-between;
    align-items: baseline;
    color: var(--gold-light);
  }
  .footer__volume, .footer__abv {
    font-family: "Arimo", sans-serif;
    font-size: 27px;
    color: #d9d2c5;
  }
  .footer__web {
    font-family: "Playfair Display", serif;
    font-size: 25px;
    color: #d9d2c5;
    letter-spacing: 0.5px;
  }
</style>
</head>
<body>
<main class="canvas">
  <section class="label">
    <div class="label__band label__band--top"></div>

    <svg class="label__art" viewBox="0 0 900 1029" xmlns="http://www.w3.org/2000/svg">
      <defs>
        <radialGradient id="ornament-glow" cx="50%" cy="50%" r="50%">
          <stop offset="0%" stop-color="#c9a574" stop-opacity="0.16"/>
          <stop offset="70%" stop-color="#c9a574" stop-opacity="0.07"/>
          <stop offset="100%" stop-color="#c9a574" stop-opacity="0"/>
        </radialGradient>
        <linearGradient id="frame-gold" x1="0" y1="0" x2="1" y2="1">
          <stop offset="0%" stop-color="#e3c99d"/>
          <stop offset="50%" stop-color="#c9a574"/>
          <stop offset="100%" stop-color="#a8834f"/>
        </linearGradient>
      </defs>
      <rect class="ornament-area" x="73" y="164" width="763" height="678" rx="60"
            fill="url(#ornament-glow)" role="img"
            aria-label="Goldene Filigran-Schnörkel rund um den Rahmen"/>
      <polygon class="gem-frame" points="225,331 683,331 785,520 458,829 129,520"
               fill="none" stroke="url(#frame-gold)" stroke-width="6" stroke-linejoin="miter"/>
      <line class="divider" x1="225" y1="583" x2="691" y2="583" stroke="#8a8070" stroke-width="1.5"/>
    </svg>

    <p class="label__text producer">KORVIX GMBH</p>
    <h1 class="label__text product-name">TANNWALDER<br>OBERKÄMMER<br>RUM</h1>
    <p class="label__text distillery">BRENNEREI BRUGGHOFER<br>FELSMATT</p>

    <footer class="footer">
      <span class="footer__volume">50 cl</span>
      <span class="footer__web">WWW.KORNTROPFEN-MUSTER.CH</span>
      <span class="footer__abv">37% Vol</span>
    </footer>

    <div class="label__band label__band--bottom"></div>
  </section>
</main>
</body>
</html>
```